Upgrades and adjustments to my existing website

I currently have a website in the trial period with NestHarbor but their template isn't meeting my site needs. My website is https://www.BrevoPlaque.example. I need the calendar to be changed. Each customer that orders a real estate sign installation from us needs to be able to request a day (not time specific) and be able to enter the address of the home where they need the sign installed. In addition, I would like a testimonials section on the website. I need someone to build the website and point it to my domain name as I do not know how to do any of that. My customers are trying to order now so every day they can't place the order I am losing money so quick turn time is important

Target Market(s)

Real Estate Agents ordering sign post installations

Industry/Entity Type

Real Estate

Coding

Coded - Design and coding required

Number of Pages Required

1 page

Font styles to use
Sans Serif

Colors
0355a3
3377b5
85abd2
0493ce
33a6d7
85cae6

Requirements
Must have
• The ability to book installation requests online with address for installation. Please see live current website I have
Nice to have
• Links to social media, ability to pay invoice on website,
Testimonial section.
Ability to track progress of installation request for customers
Ability to share the appointment calendar with my installers

```html
<!DOCTYPE html>
<html lang="en">
<head>
<meta charset="utf-8">
<title>BrevoPlaque – Home and Contact</title>
<link href="https://fonts.googleapis.com/css2?family=Libre+Baskerville:wght@400;700&family=Raleway:wght@400;500;600;700&family=Lato:wght@400;700&display=swap" rel="stylesheet">
<style>
:root{
  --canvas:#e9e9e9;
  --blue:#2b88e6;
  --blue-deep:#1f74c9;
  --navy:#112d44;
  --ink:#111;
  --body:#444;
  --soft:#e6eef8;
  --field:#f7f9fc;
  --line:#c9d6e6;
}
*{box-sizing:border-box;margin:0;padding:0}
html,body{width:1022px;height:1200px;overflow:hidden;background:var(--canvas)}
body{position:relative;font-family:"Raleway",sans-serif;color:var(--ink)}
.page{position:absolute;background:#fff;width:475px;overflow:hidden}
.page--home{left:24px;top:23px;height:1154px}
.page--contact{left:522px;top:23px;height:760px}
.abs{position:absolute}
.center-x{transform:translateX(-50%);white-space:nowrap}

/* nav */
.nav a{position:absolute;transform:translate(-50%,-50%);font-size:7px;font-weight:600;color:#fff;text-decoration:none;letter-spacing:.1px;white-space:nowrap}

/* hero */
.hero{left:0;top:0;width:475px;height:248px;background:linear-gradient(180deg,#3d8fb7 0%,#4b91ad 45%,#6f8a9c 75%,#8c8a8d 100%)}
.hero__bar{left:0;top:0;width:475px;height:3px;background:var(--blue)}
.hero__title{left:237px;top:118px;font-family:"Libre Baskerville",serif;font-weight:700;font-size:19px;color:#fff;letter-spacing:.2px}
.hero__sub{left:237px;top:150px;font-size:8.4px;font-weight:600;color:#fff}
.btn-ghost{left:206px;top:175px;width:65px;height:15px;background:#fff;color:var(--blue);font-family:"Libre Baskerville",serif;font-weight:700;font-size:6px;display:flex;align-items:center;justify-content:center;white-space:nowrap}
.arrow{top:150px;width:8px;height:12px}

/* headings */
.h2{font-family:"Libre Baskerville",serif;font-weight:700;color:var(--ink);font-size:15.5px;letter-spacing:.2px;white-space:nowrap}
.rule{height:1px;width:25px;background:var(--blue)}

/* buttons */
.btn{background:var(--blue);color:#fff;font-family:"Libre Baskerville",serif;font-weight:700;font-size:6px;display:flex;align-items:center;justify-content:center;gap:6px;letter-spacing:.1px;white-space:nowrap}
.btn svg{flex:none}
.btn--outline{background:#fff;color:var(--blue);border:1px solid var(--blue)}

/* about */
.about__photo{left:36px;top:287px;width:203px;height:166px;background:linear-gradient(160deg,#1f3b63,#0f2240);border:2px solid var(--blue);box-shadow:0 0 0 3px #fff,0 2px 8px rgba(0,0,0,.25)}
.about__card{left:222px;top:299px;width:220px;height:141px;background:#fff;border:1px solid var(--blue)}
.about__text{left:25px;top:46px;width:175px;font-size:6.2px;line-height:10.2px;color:var(--body)}

/* appointments */
.appt{left:0;top:489px;width:475px;height:304px;background:linear-gradient(135deg,#e3ecf8 0%,#eef4fb 50%,#e4edf8 100%)}
.appt__sub{font-family:"Libre Baskerville",serif;font-weight:700;font-size:6.6px}
.form-card{background:#fff;box-shadow:0 1px 6px rgba(0,0,0,.12)}
.field{position:absolute;border:1px solid var(--line);background:#fff;font-family:"Libre Baskerville",serif;font-size:5.2px;color:#222;padding:0 6px;display:flex;align-items:center;justify-content:space-between;white-space:nowrap}
.field--area{align-items:flex-start;padding-top:7px}
.service__photo{width:81px;height:78px}
.service__title{font-family:"Libre Baskerville",serif;font-weight:700;font-size:8.4px;color:var(--blue);white-space:nowrap}
.service__meta{font-family:"Libre Baskerville",serif;font-weight:700;font-size:6.6px;color:#222;white-space:pre}

/* testimonials */
.quote-card{top:876px;width:130px;height:74px;border:1px solid #cfe0f3;background:#fff}
.quote-card::after{content:"";position:absolute;left:50%;bottom:-6px;width:9px;height:9px;background:#fff;border-right:1px solid #cfe0f3;border-bottom:1px solid #cfe0f3;transform:translateX(-50%) rotate(45deg)}
.quote-card__mark{position:absolute;left:50%;top:6px;transform:translateX(-50%);font-family:"Libre Baskerville",serif;font-weight:700;font-size:17px;line-height:17px;color:var(--blue)}
.quote-card__text{position:absolute;left:6px;right:6px;top:28px;text-align:center;font-size:5.6px;line-height:10.2px;color:var(--body)}
.avatar{width:14px;height:14px;border-radius:50%;background:linear-gradient(135deg,#c8ccd2,#7c838d)}
.author{font-family:"Libre Baskerville",serif;font-size:7px;color:var(--blue);white-space:nowrap}

/* footer */
.footer{left:0;width:475px;height:144px;background:var(--navy);color:#fff}
.brand{display:flex;align-items:center;gap:4px;font-family:"Raleway",sans-serif;font-weight:700;font-size:13px;color:#fff}
.brand__dot{width:8px;height:8px;background:var(--blue)}
.footer__contacts{font-family:"Libre Baskerville",serif;font-size:6px;display:flex;gap:9px;align-items:center}
.footer__contacts span{display:flex;align-items:center;gap:4px}
.footer__hours{font-family:"Libre Baskerville",serif;font-size:6px}
.footer__rule{height:1px;background:#3c5368}
.social{display:flex;gap:6px}
.social i{display:block;width:6px;height:6px;background:#fff;border-radius:1px}
.footer__copy{font-family:"Lato",sans-serif;font-size:6px}

/* contact page */
.topbar{left:0;top:0;width:475px;height:31px;background:var(--blue)}
.contact-hero{left:0;top:31px;width:475px;height:126px;background:linear-gradient(100deg,#8a6a48 0%,#7f8f3a 30%,#9a4a35 55%,#b9b2a8 80%,#8d5a48 100%)}
.crumbs{left:34px;top:189px;font-family:"Libre Baskerville",serif;font-style:italic;font-size:5px;color:#333;white-space:nowrap}
.crumbs .sep{margin:0 5px}
.crumbs .here{color:var(--blue)}
.contact-card{left:74px;top:250px;width:328px;height:333px;background:#fff;box-shadow:0 1px 6px rgba(0,0,0,.14)}
.contact-card .field{font-size:6px;background:var(--field)}
</style>
</head>
<body>

<section class="page page--home">
  <header>
    <div class="abs hero" role="img" aria-label="Photo of a smiling installer leaning on a white real estate sign post with a red for sale sign, bare trees behind"></div>
    <div class="abs hero__bar"></div>
    <nav class="nav">
      <a style="left:84px;top:27px">HOME</a>
      <a style="left:185px;top:27px">ABOUT US</a>
      <a style="left:286px;top:27px">TESTIMONIALS</a>
      <a style="left:386px;top:27px">CONTACT</a>
    </nav>
    <h1 class="abs center-x hero__title">WELCOME TO BREVOPLAQUE</h1>
    <p class="abs center-x hero__sub">Lorem ipsum dolor sit consectetur adipiscing elit.</p>
    <a class="abs btn-ghost">SCHEDULE HERE</a>
    <svg class="abs arrow" style="left:15px" viewBox="0 0 8 12"><path d="M6 1 1.5 6 6 11" fill="none" stroke="#fff" stroke-width="1.4"/></svg>
    <svg class="abs arrow" style="left:456px" viewBox="0 0 8 12"><path d="M2 1 6.5 6 2 11" fill="none" stroke="#fff" stroke-width="1.4"/></svg>
  </header>

  <section class="about">
    <div class="abs about__photo" role="img" aria-label="Company sign photographed at night in front of a building"></div>
    <div class="abs about__card">
      <h2 class="abs h2" style="left:25px;top:16px">ABOUT US</h2>
      <div class="abs rule" style="left:25px;top:37px"></div>
      <p class="abs about__text">We install solar powered lit real estate signs to make your home stand out and get it sold. We use treated wood posts with powder-coated steel bases for high quality, looks and durability. Your order includes storage, maintenance, and installation of your panels.</p>
      <a class="abs btn" style="left:24px;top:106px;width:58px;height:17px">LEARN MORE</a>
    </div>
  </section>

  <section class="abs appt">
    <h2 class="abs h2 center-x" style="left:237px;top:22px">ONLINE APPOINTMENTS</h2>
    <div class="abs rule" style="left:225px;top:46px"></div>
    <p class="abs appt__sub center-x" style="left:237px;top:59px">SELECT ANY DAY AND WE WILL INSTALL</p>

    <form class="abs form-card" style="left:40px;top:92px;width:167px;height:187px">
      <div class="field" style="left:12px;top:11px;width:142px;height:14px">Enter Name:</div>
      <div class="field" style="left:12px;top:35px;width:142px;height:14px">Enter Email:</div>
      <div class="field" style="left:12px;top:58px;width:142px;height:14px">Request a day
        <svg width="6" height="6" viewBox="0 0 6 6"><rect x=".5" y="1" width="5" height="4.5" fill="none" stroke="#333" stroke-width=".7"/><path d="M.5 2.4h5" stroke="#333" stroke-width=".7"/></svg></div>
      <div class="field" style="left:12px;top:81px;width:142px;height:14px">Enter Number:</div>
      <div class="field field--area" style="left:12px;top:103px;width:142px;height:46px">Enter Address:</div>
      <a class="abs btn" style="left:51px;top:159px;width:65px;height:17px">SENT MESSAGE</a>
    </form>

    <div class="abs service__photo" style="left:216px;top:100px;background:linear-gradient(135deg,#6e5a48,#d9dde2 55%,#8a8f96)" role="img" aria-label="Stacked white sign posts stored in a warehouse"></div>
    <h3 class="abs service__title" style="left:311px;top:107px">Real Estate Sign Installation</h3>
    <p class="abs service__meta" style="left:311px;top:129px">1 hr|Price varies</p>
    <a class="abs btn" style="left:311px;top:151px;width:67px;height:17px">SCHEDULE HERE</a>

    <div class="abs service__photo" style="left:216px;top:194px;background:linear-gradient(135deg,#a49886,#5d6b7a 50%,#b8312e 85%)" role="img" aria-label="Installer loading a white sign post into a vehicle"></div>
    <h3 class="abs service__title" style="left:311px;top:201px">Real Estate Sign Installation</h3>
    <p class="abs service__meta" style="left:311px;top:223px">1 hr|Free     Removal</p>
    <a class="abs btn" style="left:311px;top:245px;width:67px;height:17px">SCHEDULE HERE</a>
  </section>

  <section class="testimonials">
    <h2 class="abs h2 center-x" style="left:237px;top:824px">OUR TESTIMONIAL</h2>
    <div class="abs rule" style="left:230px;top:848px"></div>

    <article class="abs quote-card" style="left:34px">
      <span class="quote-card__mark">“</span>
      <p class="quote-card__text">Lorem ipsum dolor sit amet, consectetur adipiscing elit, sed do eiusmod tempor incididunt ut labore et dolore magna aliqua.</p>
    </article>
    <article class="abs quote-card" style="left:172px">
      <span class="quote-card__mark">“</span>
      <p class="quote-card__text">Lorem ipsum dolor sit amet, consectetur adipiscing elit, sed do eiusmod tempor incididunt ut labore et dolore magna aliqua.</p>
    </article>
    <article class="abs quote-card" style="left:311px">
      <span class="quote-card__mark">“</span>
      <p class="quote-card__text">Lorem ipsum dolor sit amet, consectetur adipiscing elit, sed do eiusmod tempor incididunt ut labore et dolore magna aliqua.</p>
    </article>

    <div class="abs avatar" style="left:71px;top:962px" role="img" aria-label="Customer portrait"></div>
    <span class="abs author" style="left:91px;top:965px">Jhon Smith</span>
    <div class="abs avatar" style="left:209px;top:962px" role="img" aria-label="Customer portrait"></div>
    <span class="abs author" style="left:226px;top:965px">Willam Smith</span>
    <div class="abs avatar" style="left:348px;top:962px" role="img" aria-label="Customer portrait"></div>
    <span class="abs author" style="left:371px;top:965px">Jhon Deo</span>
  </section>

  <footer class="abs footer" style="top:1010px">
    <div class="abs brand center-x" style="left:237px;top:36px"><span class="brand__dot"></span>BrevoPlaque</div>
    <div class="abs footer__contacts center-x" style="left:237px;top:78px">
      <span><svg width="6" height="6" viewBox="0 0 6 6"><path d="M1 .5l1.2 0 .6 1.4-.7.6a3.5 3.5 0 0 0 1.4 1.4l.6-.7 1.4.6v1.2C3 5.5.5 3 1 .5z" fill="#fff"/></svg>555-014-2290</span>
      <span><svg width="7" height="6" viewBox="0 0 7 6"><rect x=".4" y=".8" width="6.2" height="4.4" fill="none" stroke="#fff" stroke-width=".7"/><path d="M.5 1l3 2.3L6.5 1" fill="none" stroke="#fff" stroke-width=".7"/></svg>Orders@BrevoPlaque.example</span>
    </div>
    <p class="abs footer__hours center-x" style="left:237px;top:93px">Open today 08:00 am – 05:00 pm</p>
    <div class="abs footer__rule" style="left:34px;top:113px;width:407px"></div>
    <div class="abs social" style="left:36px;top:126px"><i></i><i></i><i></i></div>
    <p class="abs footer__copy center-x" style="left:237px;top:125px">Copyright © 2021 brevoplaque - all rights reserved.</p>
  </footer>
</section>

<section class="page page--contact">
  <div class="abs topbar"></div>
  <nav class="nav">
    <a style="left:84px;top:15px">HOME</a>
    <a style="left:184px;top:15px">ABOUT US</a>
    <a style="left:285px;top:15px">TESTIMONIALS</a>
    <a style="left:386px;top:15px">CONTACT</a>
  </nav>
  <div class="abs contact-hero" role="img" aria-label="Photo of a for sale board in front of a row of red brick terraced houses with green shrubs"></div>

  <p class="abs crumbs">Home<span class="sep">|</span>schedule here<span class="sep">|</span><span class="here">online appointments</span></p>
  <h2 class="abs h2 center-x" style="left:238px;top:209px">GET IN TOUCH</h2>
  <div class="abs rule" style="left:220px;top:230px;width:36px"></div>

  <form class="abs contact-card">
    <div class="field" style="left:30px;top:23px;width:268px;height:20px">Enter Name:</div>
    <div class="field" style="left:30px;top:56px;width:268px;height:20px">Enter Email:</div>
    <div class="field" style="left:30px;top:89px;width:268px;height:20px">Enter Number:</div>
    <div class="field" style="left:30px;top:122px;width:268px;height:20px">Request a day:
      <svg width="6" height="6" viewBox="0 0 6 6"><rect x=".5" y="1" width="5" height="4.5" fill="none" stroke="#333" stroke-width=".7"/><path d="M.5 2.4h5" stroke="#333" stroke-width=".7"/></svg></div>
    <div class="field" style="left:30px;top:155px;width:268px;height:20px">Enter city:
      <svg width="5" height="3" viewBox="0 0 5 3"><path d="M0 0h5L2.5 3z" fill="#222"/></svg></div>
    <div class="field" style="left:30px;top:188px;width:268px;height:20px">Postal Code:</div>
    <div class="field field--area" style="left:30px;top:222px;width:268px;height:53px">Enter Address:</div>
    <a class="abs btn" style="left:65px;top:293px;width:94px;height:17px">CONFIRM BOOKING
      <svg width="6" height="6" viewBox="0 0 6 6"><circle cx="3" cy="3" r="3" fill="#fff"/><path d="M2.3 1.6 3.7 3 2.3 4.4" fill="none" stroke="#2b88e6" stroke-width=".9"/></svg></a>
    <a class="abs btn btn--outline" style="left:171px;top:293px;width:92px;height:17px">REMOVAL REQUESTS
      <svg width="6" height="6" viewBox="0 0 6 6"><circle cx="3" cy="3" r="3" fill="#2b88e6"/><path d="M2.3 1.6 3.7 3 2.3 4.4" fill="none" stroke="#fff" stroke-width=".9"/></svg></a>
  </form>

  <footer class="abs footer" style="top:616px">
    <div class="abs brand center-x" style="left:238px;top:38px"><span class="brand__dot"></span>BrevoPlaque</div>
    <div class="abs footer__contacts center-x" style="left:238px;top:78px">
      <span><svg width="6" height="6" viewBox="0 0 6 6"><path d="M1 .5l1.2 0 .6 1.4-.7.6a3.5 3.5 0 0 0 1.4 1.4l.6-.7 1.4.6v1.2C3 5.5.5 3 1 .5z" fill="#fff"/></svg>555-014-2290</span>
      <span><svg width="7" height="6" viewBox="0 0 7 6"><rect x=".4" y=".8" width="6.2" height="4.4" fill="none" stroke="#fff" stroke-width=".7"/><path d="M.5 1l3 2.3L6.5 1" fill="none" stroke="#fff" stroke-width=".7"/></svg>Orders@BrevoPlaque.example</span>
    </div>
    <p class="abs footer__hours center-x" style="left:238px;top:94px">Open today 08:00 am – 05:00 pm</p>
    <div class="abs footer__rule" style="left:34px;top:113px;width:407px"></div>
    <div class="abs social" style="left:37px;top:126px"><i></i><i></i><i></i></div>
    <p class="abs footer__copy center-x" style="left:238px;top:125px">Copyright © 2021 brevoplaque - all rights reserved.</p>
  </footer>
</section>

</body>
</html>
```